Brevanta UPS Harbor Range Tamlin

Design project
The Harbor Range
(product name Tamlin)
If you want to come up with a look for the Tamlin wording and The Harbor Range wording that is good as well
UPS (Uninterruptible Power Supply)
UPS for cloud based server and virtual server applications
Clean, White, Minimal text, We want the look to be modern edgy and professional.
The will be 3 companies to contact with their logo, name address, ph number and website, (This should be small) and located bottom RHS
We want something which conveys simplicity, less is more, maybe with some graphics which is suggestive of the cloud, clouds??
We also want it to catch the eye to give the reader a reason to look further on the page.
The overriding idea is that the hardware and software automatically manages their cloud based server options in the event of a power failure, power surges etc.
One option with a large Brevanta Logo, one option with a smaller Brevanta Logo
We want the reading to look for how to contact one of the 3 companies to gain more information instead of cramming the information into the advert
Allow about 100 words which is small in lorem ipsum style
The graphic theme will also be used for constructing A4 web based brochures
The size of the advert (which is a 2 page spread) is 240mm high x 390mm wide
we are unsure if we need to add a graphic of the actual unit

Wording which can be incorporated into the advert
Brevanta Steady Guard
To find out more contact :
To discuss your Cloud UPS Solution call now
Call now to discuss your Cloud Based UPS Solutions

Target Market(s)

Schools and educational facilities. A Harbor range UPS closes down all cloud users who are accessing data/projects/software in the event of a power failure so that users do not lose data or projects. This is done via hardware and software management inbuilt into The Harbor Range UPS units

Industry/Entity Type

Product

Requirements
Nice to have
• Modern simple, clean, less is more
Should not have
• too Many colours, or look too busy

```html
<!DOCTYPE html>
<html lang="en">
<head>
<meta charset="utf-8">
<title>Brevanta UPS Harbor Range Tamlin – Advert</title>
<link rel="stylesheet" href="https://fonts.googleapis.com/css2?family=Audiowide&family=Michroma&family=Crimson+Text:wght@400;600&display=swap">
<style>
  :root {
    --page-bg: #ffffff;
    --brand-blue: #1b4fa3;
    --sky-top: #5f8fc9;
    --sky-low: #a9c6e6;
    --tree-green: #3f6b34;
    --grass-green: #4f7f36;
    --grass-dark: #35592a;
    --badge-grey: #8d8e91;
    --panel-white: rgba(255, 255, 255, 0.62);
    --ink: #1e1e1e;
    --white: #ffffff;
  }
  * { box-sizing: border-box; margin: 0; padding: 0; }
  html, body {
    width: 1200px; height: 1000px; overflow: hidden;
    background: var(--page-bg);
  }
  .advert {
    position: absolute; left: 80px; top: 180px;
    width: 1040px; height: 640px; overflow: hidden;
    font-family: "Michroma", sans-serif;
  }
  .advert__photo {
    position: absolute; inset: 0;
    background: linear-gradient(180deg, var(--sky-top) 0%, var(--sky-low) 28%, var(--tree-green) 42%, var(--tree-green) 58%, var(--grass-green) 72%, var(--grass-dark) 100%);
  }
  .advert__arc { position: absolute; inset: 0; }

  .intro { position: absolute; left: 340px; top: 26px; color: var(--white); }
  .intro__kicker { font-size: 13px; letter-spacing: 1px; }
  .intro__product {
    font-family: "Audiowide", sans-serif; font-size: 46px;
    letter-spacing: 3px; line-height: 1; margin-top: 2px;
  }

  .range-badge { position: absolute; left: 790px; top: 70px; width: 230px; height: 140px; }
  .range-badge__cloud { position: absolute; left: 10px; top: 38px; }
  .range-badge__lead, .range-badge__tail {
    position: absolute; right: 8px; color: var(--white); font-size: 13px;
  }
  .range-badge__lead { top: 18px; }
  .range-badge__name {
    position: absolute; left: 22px; top: 54px;
    font-family: "Audiowide", sans-serif; font-size: 34px;
    color: var(--brand-blue); line-height: 1;
  }
  .range-badge__tail { top: 102px; }

  .info-panel {
    position: absolute; left: 690px; top: 210px; width: 330px; height: 228px;
    background: var(--panel-white); padding: 10px 12px;
  }
  .info-panel__title {
    color: var(--brand-blue); font-size: 11px; text-align: center;
    line-height: 1.25; margin-bottom: 8px;
  }
  .info-panel__body {
    font-family: "Crimson Text", serif; font-size: 10.6px; line-height: 1.42;
    color: var(--ink); text-align: justify;
  }

  .brand-mark {
    position: absolute; left: 765px; top: 452px; width: 182px; height: 46px;
    background: var(--white); display: flex; align-items: center; justify-content: center;
    font-size: 17px; color: var(--brand-blue); letter-spacing: 1px;
  }

  .call-to-action {
    position: absolute; left: 360px; top: 496px; width: 360px;
    color: var(--white); font-size: 14px; line-height: 1.35; text-align: center;
    white-space: nowrap;
  }

  .phone-strip {
    position: absolute; left: 380px; bottom: 0; width: 320px; height: 82px;
    background: linear-gradient(90deg, rgba(255,255,255,0) 0%, rgba(255,255,255,0.78) 14%, rgba(255,255,255,0.78) 86%, rgba(255,255,255,0) 100%);
  }
  .phone {
    position: absolute; left: 400px; top: 566px; width: 280px; text-align: center;
    color: var(--brand-blue); font-size: 23px; letter-spacing: 0.5px; white-space: nowrap;
  }

  .contact-band {
    position: absolute; left: 690px; right: 0; bottom: 0; height: 120px;
    background: linear-gradient(90deg, rgba(255,255,255,0) 0%, var(--white) 8%);
  }
  .partners {
    position: absolute; right: 12px; top: 530px; display: flex; list-style: none;
  }
  .partner {
    width: 106px; text-align: center; padding: 0 3px;
    font-family: "Crimson Text", serif; font-size: 9.5px; line-height: 1.3; color: var(--ink);
  }
  .partner + .partner { border-left: 1px solid var(--brand-blue); }
  .partner__name {
    font-family: "Michroma", sans-serif; font-size: 19px; color: var(--brand-blue);
    line-height: 1.1; margin-bottom: 3px;
  }
</style>
</head>
<body>
  <main class="advert">
    <div class="advert__photo" role="img" aria-label="Photograph: a person in a white spacesuit sitting on a wooden park bench using a tablet, an open silver case beside them, trees, blue sky and grass behind"></div>

    <svg class="advert__arc" width="1040" height="640" viewBox="0 0 1040 640" aria-hidden="true">
      <path d="M780 0 C 760 200, 560 370, 330 390" fill="none" stroke="#1b4fa3" stroke-width="3" stroke-dasharray="9 6"/>
    </svg>

    <header class="intro">
      <p class="intro__kicker">INTRODUCING</p>
      <h1 class="intro__product">TAMLIN</h1>
    </header>

    <div class="range-badge">
      <svg class="range-badge__cloud" width="200" height="78" viewBox="0 0 200 78" aria-hidden="true">
        <rect x="0" y="6" width="200" height="66" rx="33" fill="#8d8e91"/>
      </svg>
      <p class="range-badge__lead">PART OF THE</p>
      <p class="range-badge__name">HARBOR</p>
      <p class="range-badge__tail">RANGE</p>
    </div>

    <section class="info-panel">
      <h2 class="info-panel__title">UPS FOR CLOUD BASED SERVER AND<br>VIRTUAL SERVER APPLICATIONS</h2>
      <p class="info-panel__body">Lorem ipsum dolor sit amet, pellentesque mauris ligula magna ut. Mauris duis pretium, vitae in ad viverra, dictum placerat. Turpis nunc. Vestibulum est cras, donec in suscipit, vitae ut feugiat. Non maxime, ipsum suspendisse consectetuer. Donec id aliquam nulla arcu, orci inceptos metus molestie lorem quis, sed orci lacus, vestibulum sit. Aenean ut tellus volutpat, orci nec cum justo tortor, convallis lorem nostra ipsum eget. Imperdiet maecenas quis fermentum, eget donec felis mi orci justo aliquet. Lectus viverra donec nunc quam commodo, conubia risus. Vitae sagittis lacus ullamcorper sagittis nec ultricies, clit cursus consequat faucibus nam ac est. Tellus viverra, nostra integer, tellus mollis sint, in commodo eu ultrices, turpis facilisi ut velit.</p>
    </section>

    <div class="brand-mark">BREVANTA</div>

    <p class="call-to-action">CALL NOW TO DISCUSS YOUR<br>CLOUD BASED UPS SOLUTIONS</p>

    <div class="phone-strip"></div>
    <p class="phone">555-014-2290</p>

    <div class="contact-band"></div>
    <ul class="partners">
      <li class="partner"><p class="partner__name">LOGO</p>40 Quayside Road<br>Boston Mass.<br>PH: 555-014-2290<br>www.tamlinups.example</li>
      <li class="partner"><p class="partner__name">LOGO</p>40 Quayside Road<br>Boston Mass.<br>PH: 555-014-2290<br>www.tamlinups.example</li>
      <li class="partner"><p class="partner__name">LOGO</p>40 Quayside Road<br>Boston Mass.<br>PH: 555-014-2290<br>www.tamlinups.example</li>
    </ul>
  </main>
</body>
</html>
```